Harwell Lawyers Banner

I would like to have a graphic design created for a company banner. The company is Harwell Lawyers and the website is https://harwelllawyers-example.com.au/ We would like a professional banner we are able to put up at events to advertise the company.
The banner size is 800mm wide by 2000mm high so please keep the design inside these constraints.

```html
<!DOCTYPE html>
<html lang="en">
<head>
<meta charset="utf-8">
<title>Harwell Lawyers – Event Banner</title>
<link rel="stylesheet" href="https://fonts.googleapis.com/css2?family=Montserrat:wght@300;400&display=swap">
<style>
  :root {
    --backdrop: #e6e6e6;
    --banner-charcoal: #2d3034;
    --corner-grey: #45484a;
    --accent-blue: #29a0d4;
    --wordmark-white: #ffffff;
  }
  html, body {
    margin: 0;
    padding: 0;
    width: 1187px;
    height: 1200px;
    overflow: hidden;
    background: var(--backdrop);
  }
  .canvas {
    position: relative;
    width: 1187px;
    height: 1200px;
  }
  .banner {
    position: absolute;
    left: 379px;
    top: 63px;
    width: 429px;
    height: 1074px;
    background: var(--banner-charcoal);
    overflow: hidden;
  }
  .banner-shapes {
    position: absolute;
    inset: 0;
  }
  .corner-top { fill: var(--corner-grey); }
  .corner-bottom { fill: var(--accent-blue); }
  .wordmark {
    font-family: "Montserrat", sans-serif;
    font-weight: 300;
  }
  .wordmark-name {
    font-size: 175px;
    fill: var(--wordmark-white);
  }
  .wordmark-descriptor {
    font-size: 70px;
    font-weight: 400;
    fill: var(--accent-blue);
  }
  .intro {
    position: absolute;
    left: 265px;
    top: 635px;
    width: 160px;
    margin: 0;
    font-family: "Montserrat", sans-serif;
    font-weight: 400;
    font-size: 16.5px;
    line-height: 25px;
    color: var(--accent-blue);
    text-transform: uppercase;
  }
</style>
</head>
<body>
<div class="canvas">
  <section class="banner" aria-label="Harwell Lawyers event banner">
    <svg class="banner-shapes" width="429" height="1074" viewBox="0 0 429 1074" xmlns="http://www.w3.org/2000/svg">
      <polygon class="corner-top" points="0,0 171,0 0,172"/>
      <polygon class="corner-bottom" points="429,804 429,1074 159,1074"/>
      <text class="wordmark wordmark-name" transform="translate(205,93) rotate(-90)" text-anchor="end" textLength="913" lengthAdjust="spacing">HARWELL</text>
      <text class="wordmark wordmark-descriptor" transform="translate(311,96) rotate(-90)" text-anchor="end" textLength="425" lengthAdjust="spacing">LAWYERS</text>
    </svg>
    <p class="intro">Harwell Lawyers is a leading commercial law firm located in Kellan Vale, Northmoor.</p>
  </section>
</div>
</body>
</html>
```